BHG Letterhead

I need letterhead for "birch hollow gateway llc" ...

logo attached to project..

Company Info:
482 South Marigold Avenue, Suite 7D
Chicago, Illinois 60617
ofc 312-555-0148
facsimile 312-555-0193
www.birchhollowgatewayllc.example
info@birchhollowgatewayllc.example

I have multiple projects listed.. see below:

Business cards for birch hollow gateway llc
letterhead "
envelopes "

Business cards for KP Vending LLC
letterhead "
envelopes "

Industry/Entity Type

It Company

```html
<!DOCTYPE html>
<html lang="en">
<head>
<meta charset="utf-8">
<title>BHG Letterhead</title>
<link href="https://fonts.googleapis.com/css2?family=Archivo:wght@400;500&display=swap" rel="stylesheet">
<style>
  :root {
    --navy: #1f3a70;
    --paper: #ffffff;
    --backdrop: #e6e5e2;
  }
  * { margin: 0; padding: 0; box-sizing: border-box; }
  html, body {
    width: 1200px;
    height: 1000px;
    overflow: hidden;
    background: var(--backdrop);
  }
  .letterhead {
    position: absolute;
    left: 294px;
    top: 84px;
    width: 601px;
    height: 846px;
    background: var(--paper);
    font-family: "Archivo", Arial, sans-serif;
    color: var(--navy);
  }
  .contact {
    position: absolute;
    left: 40px;
    top: 78px;
    font-size: 10.5px;
    line-height: 14px;
    font-weight: 400;
  }
  .brand {
    position: absolute;
    right: 36px;
    top: 50px;
    text-align: right;
  }
  .brand-mark {
    display: inline-block;
    width: 34px;
    height: 34px;
    border-radius: 50%;
    background: var(--navy);
    margin-bottom: 6px;
  }
  .brand-name {
    font-size: 15px;
    font-weight: 500;
    letter-spacing: 0.3px;
    text-transform: uppercase;
    line-height: 18px;
  }
  .brand-web {
    font-size: 10.5px;
    font-weight: 500;
    letter-spacing: 1.6px;
    line-height: 14px;
  }
  .rule {
    position: absolute;
    left: 40px;
    width: 523px;
    height: 2px;
    background: var(--navy);
  }
  .rule-top { top: 128px; }
  .rule-bottom { top: 819px; }
</style>
</head>
<body>
  <main class="letterhead">
    <div class="contact">
      <p>Email: info@birchhollowgatewayllc.example</p>
      <p>Office: 312-555-0148 | Facsimile: 312-555-0193</p>
      <p>482 South Marigold Avenue, Suite 7D Chicago, Illinois 60617</p>
    </div>
    <div class="brand">
      <span class="brand-mark"></span>
      <p class="brand-name">Birch Hollow Gateway LLC</p>
      <p class="brand-web">www.birchhollowgatewayllc.example</p>
    </div>
    <div class="rule rule-top"></div>
    <div class="rule rule-bottom"></div>
  </main>
</body>
</html>
```